Business Card Design

Business Card for professional consulting firm working with large financial institutions.

Target Market(s)

Executive buyers

Industry/Entity Type

Banking

Contact Information for Business Card

Mild creativity wanted. Not boring, but do elaborate artwork.

Font styles to use
Serif
Sans Serif

Colors

Designer to choose colors to be used in the design.

Requirements
Must have
• Standard business card features - company name, individual name, telephone, website, email, locations.
Nice to have
• Two colors
Should not have
• too many colors, fancy printing, cartoons.

```html
<!DOCTYPE html>
<html lang="en">
<head>
<meta charset="UTF-8">
<title>Veritan Advisory – Business Card</title>
<link rel="stylesheet" href="https://fonts.googleapis.com/css2?family=Crimson+Text:wght@400&family=Michroma&display=swap">
<style>
  :root {
    --backdrop: #959595;
    --ink: #111111;
    --paper: #ffffff;
    --muted: #cfcfcf;
    --serif: "Crimson Text", Georgia, serif;
    --sans: "Michroma", Arial, sans-serif;
  }
  * { box-sizing: border-box; margin: 0; padding: 0; }
  html, body {
    width: 1200px; height: 1200px; overflow: hidden;
    background: var(--backdrop);
  }
  .sheet {
    width: 1200px; height: 1200px;
    display: flex; flex-direction: column; align-items: center; justify-content: center;
    gap: 60px;
  }
  .card {
    width: 840px; height: 480px;
    position: relative; overflow: hidden;
    box-shadow: 0 10px 24px rgba(0,0,0,0.25);
  }

  /* Front */
  .card--front {
    background: radial-gradient(ellipse at 50% 45%, #262626 0%, var(--ink) 70%);
    display: flex; align-items: center; justify-content: center;
  }
  .wordmark {
    font-family: var(--serif);
    font-weight: 400;
    color: var(--paper);
    letter-spacing: 1px;
  }
  .card--front .wordmark { font-size: 72px; }

  /* Back */
  .card--back { background: var(--ink); display: flex; }
  .brand-band {
    width: 236px; height: 100%;
    background: var(--paper);
    display: flex; align-items: center; justify-content: center;
  }
  .brand-band .wordmark {
    color: var(--ink);
    font-size: 40px;
    white-space: nowrap;
    transform: rotate(-90deg);
  }
  .details {
    flex: 1;
    padding: 150px 46px 0 0;
    display: flex; flex-direction: column; align-items: flex-end;
  }
  .name-box {
    border: 2px solid var(--paper);
    padding: 10px 16px 8px;
  }
  .name {
    font-family: var(--sans);
    color: var(--paper);
    font-size: 32px;
    letter-spacing: 1px;
    text-transform: uppercase;
    white-space: nowrap;
  }
  .role {
    font-family: var(--serif);
    color: var(--muted);
    font-size: 20px;
    margin-top: 4px;
    margin-right: 4px;
  }
  .contact {
    list-style: none;
    margin-top: 46px;
    display: flex; flex-direction: column; align-items: flex-end; gap: 4px;
  }
  .contact li {
    display: flex; align-items: center; gap: 10px;
    font-family: var(--serif);
    color: var(--paper);
    font-size: 21px;
  }
  .contact svg { width: 18px; height: 18px; fill: var(--paper); flex: none; }
</style>
</head>
<body>
<main class="sheet">
  <section class="card card--front" aria-label="Card front">
    <span class="wordmark">Veritan Advisory</span>
  </section>

  <section class="card card--back" aria-label="Card back">
    <div class="brand-band">
      <span class="wordmark">Veritan Advisory</span>
    </div>
    <div class="details">
      <div class="name-box"><h1 class="name">Daniel Harlow</h1></div>
      <p class="role">Manager</p>
      <ul class="contact">
        <li>555.014.7720
          <svg viewBox="0 0 24 24" aria-hidden="true"><path d="M6.6 10.8a15 15 0 0 0 6.6 6.6l2.2-2.2a1 1 0 0 1 1-.25 11.4 11.4 0 0 0 3.6.57 1 1 0 0 1 1 1V20a1 1 0 0 1-1 1A17 17 0 0 1 3 4a1 1 0 0 1 1-1h3.5a1 1 0 0 1 1 1c0 1.25.2 2.45.57 3.57a1 1 0 0 1-.25 1z"/></svg>
        </li>
        <li>harlow@veritanadvisory.com
          <svg viewBox="0 0 24 24" aria-hidden="true"><path d="M2 5h20v14H2zm2 2v.5l8 5 8-5V7zm0 2.8V17h16V9.8l-8 5z"/></svg>
        </li>
        <li>www.veritanadvisory.com
          <svg viewBox="0 0 24 24" aria-hidden="true"><path d="M12 2a10 10 0 1 0 0 20 10 10 0 0 0 0-20zm6.9 6h-3a15 15 0 0 0-1.3-3.6A8 8 0 0 1 18.9 8zM12 4c.8 1.1 1.5 2.5 1.9 4h-3.8c.4-1.5 1.1-2.9 1.9-4zM4.3 14a8 8 0 0 1 0-4h3.4a16 16 0 0 0 0 4zm.8 2h3a15 15 0 0 0 1.3 3.6A8 8 0 0 1 5.1 16zM8 8H5.1a8 8 0 0 1 4.3-3.6C8.8 5.5 8.4 6.7 8 8zm4 12c-.8-1.1-1.5-2.5-1.9-4h3.8c-.4 1.5-1.1 2.9-1.9 4zm2.3-6H9.7a14 14 0 0 1 0-4h4.6a14 14 0 0 1 0 4zm.3 5.6c.6-1.1 1-2.3 1.3-3.6h3a8 8 0 0 1-4.3 3.6zm1.7-5.6a16 16 0 0 0 0-4h3.4a8 8 0 0 1 0 4z"/></svg>
        </li>
        <li>1280 Marlow Street, Fairview, KY, 40190
          <svg viewBox="0 0 24 24" aria-hidden="true"><path d="M12 3 2 12h3v8h5v-5h4v5h5v-8h3z"/></svg>
        </li>
      </ul>
    </div>
  </section>
</main>
</body>
</html>
```